Business Card Design

I run an executive search and head hunting company.
My areas of business is within financial services and I cover, primarily sales and trading.

I am looking for a double sided, black business card and would like to keep the design fairly simple. Name to front and details on the reverse.

I would require a logo - some logo ideas.

*****Just some idea I am playing with - a white out halo over the "i" in Corwin.
A quill or feather somewhere within the layout. Above the Corwin Hale & Tate ? beneath it ? etc......

I have attached something I quite like but the whole creativity and layout is down to you. I am thinking to have the "&" in between Corwin Hale & Tate, maybe white out perhaps and may have it spot gloss uv'd when it comes to print.

I am pretty open minded though !

Target Market(s)

financial services - brokers and investment banking

Industry/Entity Type

Financial

Contact Information for Business Card

Corwin Hale & Tate
No 7 The Yard
31 Poplin Avenue
Brentwood
Essex
CM19 8QT

Telephone - + 44 (0)1277 555 019
Mobile -+ 44 (0) 7700 934 162
email - owen@corwinhaletate.co.uk
web - www.corwinhaletate.co.uk

Owen Tate
Managing Director

Colors

Designer to choose colors to be used in the design.

Requirements
Should not have
• Finance - brokers investment banking.

```html
<!DOCTYPE html>
<html lang="en">
<head>
<meta charset="utf-8">
<title>Corwin Hale &amp; Tate — Business Card</title>
<link rel="stylesheet" href="https://fonts.googleapis.com/css2?family=Oxanium:wght@500;600&family=Saira+Condensed:wght@600&family=Aldrich&display=swap">
<style>
  :root {
    --backdrop: #9a9a9a;
    --brand-black: #16171b;
    --rule-grey: #4a4b52;
    --panel-light: #f4f4f5;
    --panel-shade: #d6d7da;
    --ink: #1f2024;
    --ink-soft: #55565c;
    --paper: #ffffff;
  }
  * { box-sizing: border-box; margin: 0; padding: 0; }
  html, body { width: 1200px; height: 894px; overflow: hidden; }
  body {
    background: var(--backdrop);
    display: flex;
    align-items: center;
    justify-content: center;
    gap: 40px;
  }
  .card {
    position: relative;
    width: 540px;
    height: 310px;
    overflow: hidden;
  }

  /* Reverse side: contact details */
  .card--details { background: var(--brand-black); }
  .card__panel {
    position: absolute;
    left: 0; right: 0;
    top: 46px; height: 180px;
    background: radial-gradient(ellipse at 45% 45%, var(--panel-light) 0%, #ececee 45%, var(--panel-shade) 100%);
    border-top: 6px solid var(--rule-grey);
    border-bottom: 6px solid var(--rule-grey);
  }
  .card__name-bar {
    position: absolute;
    left: 0; top: 64px;
    width: 56px; height: 24px;
    background: var(--brand-black);
  }
  .card__identity {
    position: absolute;
    left: 64px; top: 36px;
    width: 210px;
  }
  .card__name {
    font-family: "Saira Condensed", sans-serif;
    font-weight: 600;
    font-size: 44px;
    line-height: 0.95;
    letter-spacing: 1px;
    color: var(--brand-black);
    white-space: nowrap;
  }
  .card__role {
    font-family: "Aldrich", sans-serif;
    font-size: 10.5px;
    letter-spacing: 1.4px;
    color: var(--ink-soft);
    margin-top: 3px;
  }
  .card__web {
    display: inline-block;
    margin-top: 5px;
    padding: 3px 10px 3px 8px;
    background: var(--brand-black);
    color: var(--paper);
    font-family: "Aldrich", sans-serif;
    font-size: 9px;
    letter-spacing: 0.4px;
    white-space: nowrap;
  }
  .contact-list {
    position: absolute;
    left: 290px; top: 18px;
    width: 240px;
    list-style: none;
  }
  .contact-list__item {
    display: flex;
    align-items: center;
    gap: 10px;
    min-height: 36px;
    margin-bottom: 8px;
    font-family: "Aldrich", sans-serif;
    font-size: 11px;
    line-height: 1.3;
    color: var(--ink);
    white-space: nowrap;
  }
  .contact-list__icon {
    flex: none;
    width: 28px; height: 28px;
    border-radius: 50%;
    background: var(--brand-black);
    display: flex;
    align-items: center;
    justify-content: center;
  }

  /* Front side: firm name */
  .card--front {
    background: var(--brand-black);
    display: flex;
    align-items: center;
    justify-content: center;
  }
  .card__firm {
    font-family: "Oxanium", sans-serif;
    font-weight: 600;
    font-size: 30px;
    font-variant: small-caps;
    letter-spacing: 2px;
    color: var(--paper);
  }
</style>
</head>
<body>

  <section class="card card--details" aria-label="Card reverse with contact details">
    <div class="card__panel">
      <div class="card__name-bar"></div>
      <div class="card__identity">
        <h1 class="card__name">OWEN TATE</h1>
        <p class="card__role">MANAGING DIRECTOR</p>
        <p class="card__web">www.corwinhaletate.co.uk</p>
      </div>
      <ul class="contact-list">
        <li class="contact-list__item">
          <span class="contact-list__icon">
            <svg width="16" height="16" viewBox="0 0 16 16" aria-hidden="true">
              <path d="M2 8 L8 2.5 L14 8" fill="none" stroke="#fff" stroke-width="1.6" stroke-linejoin="round"/>
              <path d="M4 7.5 V13.5 H12 V7.5" fill="none" stroke="#fff" stroke-width="1.6"/>
              <rect x="7" y="10" width="2" height="3.5" fill="#fff"/>
            </svg>
          </span>
          <span>No 7 The Yard<br>31 Poplin Avenue, Brentwood<br>Essex CM19 8QT</span>
        </li>
        <li class="contact-list__item">
          <span class="contact-list__icon">
            <svg width="16" height="16" viewBox="0 0 16 16" aria-hidden="true">
              <rect x="4.5" y="1.5" width="7" height="13" rx="1.4" fill="none" stroke="#fff" stroke-width="1.4"/>
              <line x1="7" y1="12.3" x2="9" y2="12.3" stroke="#fff" stroke-width="1.2"/>
            </svg>
          </span>
          <span>T + 44 (0)1277 555 019<br>M + 44 (0) 7700 934 162</span>
        </li>
        <li class="contact-list__item">
          <span class="contact-list__icon">
            <svg width="16" height="16" viewBox="0 0 16 16" aria-hidden="true">
              <rect x="2" y="4" width="12" height="8.5" fill="none" stroke="#fff" stroke-width="1.4"/>
              <path d="M2 4 L8 9 L14 4" fill="none" stroke="#fff" stroke-width="1.4"/>
            </svg>
          </span>
          <span>owen@corwinhaletate.co.uk</span>
        </li>
      </ul>
    </div>
  </section>

  <section class="card card--front" aria-label="Card front with firm name">
    <p class="card__firm">Corwin Hale &amp; Tate</p>
  </section>

</body>
</html>
```